Lawn Sign Design – Brisko

We need a clean, eye-catching 18" x 24" lawn sign for Brisko that effectively communicates our core message while maintaining strong brand consistency.

Key Elements to Include:
Tagline (Main Focus): Upgrade Your Roof Without Replacing It
Website: www.tryvexlo-demo.example
Phone Number: (877) BRISKO-GO
RQMH License Number: 4830516
Brisko Logo & Branding: Ensure the logo, corporate colors, and custom font are used consistently to align with our existing branding.

Design Guidelines:
Simple & High-Impact: The tagline should be the most prominent element on the sign, drawing immediate attention.
Easy Readability: Use a bold, clean design with high contrast for quick readability from a distance.
Balanced Layout: Place supporting details (website, phone number, and RQMH number) in a visually clear but secondary position to the tagline.
Professional & Modern: The sign should reflect credibility and innovation in the roofing industry.

Deliverables:
High-resolution print-ready files (CMYK)
A digital proof for review before finalizing
The final design should make a strong impression with minimal text, ensuring that anyone passing by can instantly grasp what we offer.

I am including our custom font. To get an hexagon in our name, simply type the $ after the 'O" Please use this font for anything you type.

```html
<!DOCTYPE html>
<html lang="en">
<head>
<meta charset="utf-8">
<title>Brisko Lawn Sign</title>
<link rel="stylesheet" href="https://fonts.googleapis.com/css2?family=Nunito:wght@700;800;900&display=swap">
<style>
  :root {
    --brand-blue: #0f4f9b;
    --brand-blue-soft: #5b86c0;
    --ink: #0b0b0b;
    --paper: #ffffff;
    --backdrop: #e9ecf0;
  }
  html, body {
    margin: 0;
    padding: 0;
    width: 1200px;
    height: 853px;
    overflow: hidden;
    background: var(--backdrop);
  }
  .lawn-sign {
    position: absolute;
    left: 60px;
    top: 21px;
    width: 1080px;
    height: 811px;
    background: var(--paper);
    box-shadow: 0 2px 8px rgba(0,0,0,0.15);
  }
  .lawn-sign svg { display: block; width: 100%; height: 100%; }
  .sign-text { font-family: "Nunito", sans-serif; }
  .brand-name { fill: var(--brand-blue); font-weight: 900; font-size: 86px; letter-spacing: 3px; }
  .band-word { fill: var(--paper); font-weight: 800; }
  .headline-blue { fill: var(--brand-blue); font-weight: 800; }
  .headline-black { fill: var(--ink); font-weight: 900; }
  .call-label { fill: var(--brand-blue); font-weight: 800; }
  .call-number { fill: var(--ink); font-weight: 800; }
  .license-text { fill: var(--paper); font-weight: 800; font-size: 13px; }
  .website { fill: var(--paper); font-weight: 800; font-size: 34px; letter-spacing: 3px; }
  .band-ink { fill: var(--ink); }
  .band-blue { fill: var(--brand-blue); }
</style>
</head>
<body>
<div class="lawn-sign">
  <svg viewBox="0 0 932 700" xmlns="http://www.w3.org/2000/svg" class="sign-text">
    <defs>
      <linearGradient id="roof-tone" x1="0" y1="0" x2="1" y2="0">
        <stop offset="0" stop-color="var(--ink)" stop-opacity="0.85"/>
        <stop offset="1" stop-color="var(--brand-blue)"/>
      </linearGradient>
    </defs>

    <text class="brand-name" x="466" y="130" text-anchor="middle">Brisko</text>

    <polygon class="band-ink" points="148,290 240,218 565,218 485,290"/>
    <text class="band-word" x="356" y="272" text-anchor="middle" font-size="48">UPGRADE</text>

    <rect class="roof-illustration" x="492" y="210" width="300" height="80" fill="url(#roof-tone)" role="img" aria-label="House roof illustration"/>

    <polygon class="band-ink" points="217,307 407,307 407,353 272,353"/>
    <text class="band-word" x="332" y="347" text-anchor="middle" font-size="42">YOUR</text>
    <text class="headline-blue" x="410" y="387" font-size="112" textLength="320" lengthAdjust="spacingAndGlyphs">ROOF</text>

    <polygon class="band-blue" points="47,400 382,400 382,457 113,457"/>
    <text class="band-word" x="238" y="450" text-anchor="middle" font-size="54">WITHOUT</text>
    <text class="headline-black" x="393" y="455" font-size="72" textLength="408" lengthAdjust="spacingAndGlyphs">REPLACING</text>
    <text class="headline-blue" x="818" y="455" font-size="72" textLength="66" lengthAdjust="spacingAndGlyphs">IT</text>

    <text x="127" y="591" font-size="40">
      <tspan class="call-label">CALL:</tspan>
      <tspan class="call-number">(877) BRISKO-GO</tspan>
    </text>

    <polygon class="band-ink" points="625,598 662,557 932,557 932,598"/>
    <text class="license-text" x="780" y="584" text-anchor="middle">RQMH License Number: 4830516</text>

    <rect class="band-blue" x="0" y="598" width="932" height="102"/>
    <text class="website" x="466" y="652" text-anchor="middle">www.tryvexlo-demo.example</text>
  </svg>
</div>
</body>
</html>
```